Letterhead Design for Law Firm

**Edit: I have added the photo of a bottom that I like.

------
We are looking for a re-design of our new letterhead. The letterhead is for a law firm and will be used for digital and traditionally printed correspondence.

Here are some suggestions:

- Please use colours are #8ec900 and simple black.
- Please do not use any type of "waves" at the bottom of the page. This is not in style at all.
- Please stay modern yet conservative.
- Please use font Segoe UI Light or similar if you can
- Avoid clipart or illustrations.
- Utilize ample white space in the layout so the design looks clean and information is easy to read at a glance. Don't overcrowd the letterhead.
- Make sure the letterhead design is consistent with our brand identity (see brambleford.ca)
-Please, no black headers or footers.

I am attaching my current letterhead and signature for your convenience.

Remember, the letterhead is an extension of our professional identity. We are a successful firm and trial lawyers who correspond with insurers, judges, lawyers, courts, clients, etc. Make it new, modern, attractive, yet powerful and conservative.

It needs to be easily printable. I would like the bleed removed in print so the black bar the bottom crosses the page (but the text is not near the edges)

Target Market(s)

Clients, Government Offices, Judiciary, Lawyers, Insurance Companies, Colleagues.

Industry/Entity Type

Law

Font styles to use
Other font styles liked:
• Segoe UI LIght, Calibri Light,

Colors
00AB8E
00BBA5
67D7C9
C6EFE9
E9F9F6

Requirements
Must have
• Everything that is on the letterhead now.
Nice to have
• Cutting Edge design, yet conservative.
Should not have
• law firm cliche design, images,

```html
<!DOCTYPE html>
<html lang="en">
<head>
<meta charset="utf-8">
<title>Meridale – Letterhead</title>
<link rel="stylesheet" href="https://fonts.googleapis.com/css2?family=Noto+Sans:wght@300;700&display=swap">
<style>
  :root {
    --brand-green: #8ec900;
    --ink: #000000;
    --text-grey: #333333;
    --paper: #fdfdfd;
  }
  html, body {
    margin: 0;
    padding: 0;
    overflow: hidden;
    background: var(--paper);
  }
  .letterhead {
    position: relative;
    width: 849px;
    height: 1200px;
    background: var(--paper);
    font-family: "Noto Sans", "Segoe UI", sans-serif;
    overflow: hidden;
  }
  .firm-name {
    position: absolute;
    left: 37px;
    top: 56px;
    width: 302px;
    margin: 0;
    font-weight: 300;
    font-size: 60px;
    line-height: 80px;
    color: var(--ink);
    text-align: center;
  }
  .practice-areas {
    position: absolute;
    left: 657px;
    top: 48px;
    font-size: 13.5px;
    line-height: 16.4px;
    font-weight: 300;
    color: var(--text-grey);
  }
  .practice-areas h2 {
    margin: 0;
    font-size: 13.5px;
    line-height: 17px;
    font-weight: 700;
    color: var(--brand-green);
  }
  .practice-areas ul {
    list-style: none;
    margin: 0;
    padding: 0;
  }
  .side-bar {
    position: absolute;
    left: 0;
    top: 249px;
    width: 36px;
  }
  .footer {
    position: absolute;
    left: 36px;
    top: 1115px;
    width: 786px;
    height: 80px;
    border-top: 2px solid var(--brand-green);
  }
  .footer-col {
    position: absolute;
    top: 8px;
    transform: translateX(-50%);
    text-align: center;
    white-space: nowrap;
    font-size: 13.5px;
    font-weight: 300;
    line-height: 17px;
    color: var(--text-grey);
  }
  .footer-col h3 {
    margin: 0 0 1px;
    font-size: 15px;
    line-height: 19px;
    font-weight: 700;
    color: var(--brand-green);
  }
  .footer-col p { margin: 0; }
  .col-address { left: 108px; }
  .col-contact { left: 280px; }
  .col-website { left: 424px; }
  .col-email   { left: 561px; }
  .col-clerk   { left: 701px; }
</style>
</head>
<body>
<div class="letterhead">
  <header>
    <h1 class="firm-name">Meridale</h1>
    <section class="practice-areas">
      <h2>Practice Restricted:</h2>
      <ul>
        <li>Serious Personal Injury</li>
        <li>Wrongful Death Litigation</li>
        <li>Long-Term Disability Litigation</li>
        <li>Wrongful Dismissal Litigation</li>
        <li>Employee Terminations</li>
      </ul>
    </section>
  </header>

  <svg class="side-bar" width="36" height="747" viewBox="0 0 36 747" aria-hidden="true">
    <rect x="0" y="0" width="36" height="5" fill="var(--brand-green)"/>
    <rect x="0" y="5" width="36" height="531" fill="var(--ink)"/>
    <rect x="0" y="536" width="36" height="211" fill="var(--brand-green)"/>
  </svg>

  <footer class="footer">
    <div class="footer-col col-address">
      <h3>Address</h3>
      <p>48 Orchard Lane W., Suite</p>
      <p>1210 Ashbury, ON&nbsp; L9T 2B6</p>
    </div>
    <div class="footer-col col-contact">
      <h3>Contact</h3>
      <p>905-555-0142</p>
      <p>905-555-0187 (Fax)</p>
    </div>
    <div class="footer-col col-website">
      <h3>Website</h3>
      <p>www.brambleford.ca</p>
    </div>
    <div class="footer-col col-email">
      <h3>Email</h3>
      <p>clara@brambleford.ca</p>
    </div>
    <div class="footer-col col-clerk">
      <h3>File Clerk</h3>
      <p>Clara Whitlow</p>
    </div>
  </footer>
</div>
</body>
</html>
```